Tavner Golf Academy Brochure Design Project

We need a tri- fold brochure for our golf academy. Tavner Golf Academy was founded by Dale Tavner, a strength coach on the NLK Circuit. Our Academy fuses Swing instruction, 3D biomechanic analysis and fitness training. We would like to incorporate the colors green, grey/silver and possible black. The final design should communicate movement/action and health.
Updates
The brochure is tri fold, double sided. Front cover should include logo, and a photo of a golfer. inside should include a a history of our company, and the services we offer(I will provide). Back middle panel should be white, with logo on the top and space for address and contact info on the bottom (we currently have 2 locations, and may want to tailor this information). The other fold in should include testamonials (I will provide). Thank you.
Include the following Titles, pictures and descriptions under 'Service'
Industry/Entity Type
Fitness
Requirements
Must have
- photos of people recieving golf instruction, people performing functional exercise training (stability balls, tubing, medicine balls, stretching) We would like to designate a space to give a description of each of our services: 1)Golf Performance Evaluation. 2)Swing Coaching. 3)3D and Video Feedback Coaching. 4)Golf Performance (fitness) Coaching.
Testimonials from the Pros:
“I have trained exclusively with Dale for the last several years. Under his guidance, I have greatly enhanced my power, flexibility, and endurance on the course. As Head Strength and Conditioning Coach for the NLK, Dale personalizes cutting-edge golf fitness programs for me, so I know that every day I play, I am at the top of my game. As Dale’s fitness student and friend, I will thoroughly enjoy watching him create one of the world’s foremost golf performance companies.” - Tod Bramwell, 16 time NLK Circuit winner, Winner of the 2003 Corvane Classic, 2010 Halvery Trophy Champion
“Dale has really helped me take my golf fitness to the next level. Preventing injury, strength training, stability, flexibility, and generating power are some of the areas we have worked on and improved!” - Matías Orduna, 3 time NLK Circuit winner, 3 time Westmarch State College All American, 2 time MVC Player of the Year
“Dale Tavner is one of the most knowledgeable and enthusiastic trainers in the business. Whether it be golf specific, bust your butt or light stretching, Dale has a varied, experienced and fun way to train!”- Glen Purdey, Winner, 2005 Morton Quill Award, 8 time NLK Circuit winner, 20 professional wins
“I trust and rely on Dale to get me ready for every round of golf that I play on the NLK Circuit. He is definitely one of the best in the industry.”- Wendell Pruitt, NLK Circuit Professional Golfer, Winner, 2007 Lyle Dunmore Vantrex Invitational, 2010 Ostrava Mutual Championship
“Since I started working with Dale my endurance, flexibility and strength have improved dramatically. His golf specific program has really shored up the weak areas of my body. He has also really helped me come back from my knee and back injuries.” - Lonnie Gressett, 4 time NLK Circuit Winner

```html
<!DOCTYPE html>
<html lang="en">
<head>
<meta charset="utf-8">
<title>Tavner Golf Academy – Brochure Inside</title>
<link rel="stylesheet" href="https://fonts.googleapis.com/css2?family=Carlito:wght@400;700&family=Pinyon+Script&display=swap">
<style>
:root{
  --green:#0c8a55;
  --green-dark:#0a7a4b;
  --green-line:#138a59;
  --grey:#8e8e8e;
  --grey-band:#bdbdbd;
  --ink:#1e1e1e;
  --white:#ffffff;
  --rule:#bfe3df;
}
*{margin:0;padding:0;box-sizing:border-box}
html,body{width:1200px;height:928px;overflow:hidden;background:var(--white)}
.brochure{position:relative;width:1200px;height:928px;overflow:hidden;font-family:"Carlito",Calibri,Arial,sans-serif;color:var(--ink)}
.panel{position:absolute;top:0;height:928px;width:400px}
.panel--history{left:0;background:linear-gradient(to bottom,var(--green) 0,var(--green) 150px,#3a9f72 300px,#cfe8dc 480px,var(--white) 640px)}
.panel--services{left:400px;background:var(--white)}
.panel--testimonials{left:800px;background:linear-gradient(to bottom,var(--grey) 0,#a9a9a9 260px,#dedede 520px,var(--white) 700px)}
.panel-title{position:absolute;top:56px;font-weight:400;font-size:24px;line-height:31px;color:var(--white)}
.panel--history .panel-title{left:47px}
.panel--services .panel-title{left:38px;color:var(--green)}
.panel--testimonials .panel-title{left:40px}
.history-photo{position:absolute;left:47px;top:137px;width:311px;height:151px;background:linear-gradient(135deg,#e9f1f4 0,#c9d7de 45%,#2a3240 70%,#d8e2e6 100%)}
.quote{position:absolute;font-size:15px;line-height:20px}
.history-quote-1{left:47px;top:313px;width:315px}
.history-quote-2{left:47px;top:494px;width:315px}
.tagline{position:absolute;left:74px;top:640px;font-family:"Pinyon Script",cursive;font-size:31px;color:var(--ink)}
.service{position:absolute;left:19px;width:359px}
.service-title{margin-left:19px;font-size:17px;line-height:22px;font-weight:400}
.service-body{display:flex;gap:14px;margin:12px 0 0 19px}
.service-photo{flex:none;width:89px;height:79px}
.service-text{font-size:15px;line-height:20px;width:225px}
.service-rule{position:absolute;left:19px;width:359px;height:1px;background:var(--rule)}
.photo-sky{background:linear-gradient(to bottom,#5b8fd0 0,#a8c7ea 45%,#4f9a3a 60%,#2f7a23 100%)}
.photo-course{background:linear-gradient(to bottom,#7aa0c8 0,#9fbf8a 30%,#5f9a3c 55%,#3c7d28 100%)}
.photo-turf{background:linear-gradient(135deg,#5a9a32 0,#3f7d22 60%,#2f6a1a 100%)}
.photo-green{background:linear-gradient(to bottom,#c7dcef 0,#8bb36a 35%,#4f8f2c 70%,#356f1e 100%)}
.testimonial-1{left:40px;top:104px;width:340px}
.testimonial-2{left:40px;top:383px;width:340px}
.testimonial-3{left:40px;top:561px;width:340px}
.wave{position:absolute;left:0;top:0;width:1200px;height:928px}
.snapshot{position:absolute;background:var(--white);padding:4px 4px 12px;box-shadow:1px 2px 5px rgba(0,0,0,.35)}
.snapshot span{display:block;width:100%;height:100%;background:linear-gradient(to bottom,#8fb0cf 0,#7aa36a 55%,#3e7a2a 100%)}
.snap-1{left:101px;top:742px;width:74px;height:86px;transform:rotate(-4deg)}
.snap-2{left:234px;top:792px;width:61px;height:74px;transform:rotate(3deg)}
.snap-3{left:539px;top:806px;width:94px;height:70px;transform:rotate(2deg)}
.snap-4{left:878px;top:725px;width:64px;height:77px;transform:rotate(5deg)}
.snap-5{left:1028px;top:708px;width:76px;height:80px;transform:rotate(-3deg)}
</style>
</head>
<body>
<main class="brochure">
  <section class="panel panel--history">
    <h2 class="panel-title">History of<br>Our Company</h2>
    <div class="history-photo" role="img" aria-label="Photo of three smiling business people around a laptop in a bright office"></div>
    <p class="quote history-quote-1">“I trust and rely on Dale to get me ready for every round of golf that I play on the NLK Circuit. He is definitely one of the best in the industry.”- Wendell Pruitt, NLK Circuit Professional Golfer, Winner, 2007 Lyle Dunmore Vantrex Invitational, 2010 Ostrava Mutual Championship</p>
    <p class="quote history-quote-2">“Since I started working with Dale my endurance, flexibility and strength have improved dramatically. His golf specific program has really shored up the weak areas of my body. He has also really helped me come back from my knee and back injuries.” - Lonnie Gressett, 4 time NLK Circuit Winner</p>
  </section>

  <section class="panel panel--services">
    <h2 class="panel-title">Our<br>Services</h2>
    <article class="service" style="top:128px">
      <h3 class="service-title">Golf Performance Evaluation.</h3>
      <div class="service-body">
        <div class="service-photo photo-sky" role="img" aria-label="Photo of a driver head addressing a ball on a tee"></div>
        <p class="service-text">I trust and rely on Dale to get me ready for every round of golf that I play on the NLK Circuit.</p>
      </div>
    </article>
    <div class="service-rule" style="top:262px"></div>
    <article class="service" style="top:270px">
      <h3 class="service-title">Swing Coaching.</h3>
      <div class="service-body">
        <div class="service-photo photo-course" role="img" aria-label="Photo of a golfer mid-swing on a fairway"></div>
        <p class="service-text">I trust and rely on Dale to get me ready for every round of golf that I play on the NLK Circuit.</p>
      </div>
    </article>
    <div class="service-rule" style="top:402px"></div>
    <article class="service" style="top:411px">
      <h3 class="service-title">3D and Video Feedback Coaching.</h3>
      <div class="service-body">
        <div class="service-photo photo-turf" role="img" aria-label="Photo of a sequence of golf balls rolling across turf"></div>
        <p class="service-text">I trust and rely on Dale to get me ready for every round of golf that I play on the NLK Circuit.</p>
      </div>
    </article>
    <div class="service-rule" style="top:544px"></div>
    <article class="service" style="top:553px">
      <h3 class="service-title">Golf Performance (fitness) Coaching.</h3>
      <div class="service-body">
        <div class="service-photo photo-green" role="img" aria-label="Photo of a gloved hand placing a ball on the green"></div>
        <p class="service-text">I trust and rely on Dale to get me ready for every round of golf that I play on the NLK Circuit.</p>
      </div>
    </article>
  </section>

  <section class="panel panel--testimonials">
    <h2 class="panel-title">Testimonials</h2>
    <p class="quote testimonial-1">“I have trained exclusively with Dale for the last several years. Under his guidance, I have greatly enhanced my power, flexibility, and endurance on the course. As Head Strength and Conditioning Coach for the NLK, Dale personalizes cutting-edge golf fitness programs for me, so I know that every day I play, I am at the top of my game. As Dale’s fitness student and friend, I will thoroughly enjoy watching him create one of the world’s foremost golf performance companies.” - Tod Bramwell, 16 time NLK Circuit winner, Winner of the 2003 Corvane Classic, 2010 Halvery Trophy Champion</p>
    <p class="quote testimonial-2">“Dale has really helped me take my golf fitness to the next level. Preventing injury, strength training, stability, flexibility, and generating power are some of the areas we have worked on and improved!” - Matías Orduna, 3 time NLK Circuit winner, 3 time Westmarch State College All American, 2 time MVC Player of the Year</p>
    <p class="quote testimonial-3">“Dale Tavner is one of the most knowledgeable and enthusiastic trainers in the business. Whether it be golf specific, bust your butt or light stretching, Dale has a varied, experienced and fun way to train!”- Glen Purdey, Winner, 2005 Morton Quill Award, 8 time NLK Circuit winner, 20 professional wins</p>
  </section>

  <svg class="wave" viewBox="0 0 1200 928" aria-hidden="true">
    <path d="M0,690 C220,790 430,848 640,842 C850,836 1010,750 1200,706 L1200,928 L0,928 Z" fill="var(--grey-band)"/>
    <path d="M150,808 C330,850 480,872 640,866 C850,858 1010,770 1200,728" fill="none" stroke="var(--white)" stroke-width="14"/>
    <path d="M150,808 C330,850 480,872 640,866 C850,858 1010,770 1200,728" fill="none" stroke="var(--green-line)" stroke-width="3"/>
  </svg>

  <div class="snapshot snap-1" role="img" aria-label="Snapshot of a professional golfer finishing a swing"><span></span></div>
  <div class="snapshot snap-2" role="img" aria-label="Snapshot of a golfer crouching to read a putt"><span></span></div>
  <div class="snapshot snap-3" role="img" aria-label="Snapshot of a golfer lying low on the green to read the line"><span></span></div>
  <div class="snapshot snap-4" role="img" aria-label="Snapshot of a golfer holding a trophy"><span></span></div>
  <div class="snapshot snap-5" role="img" aria-label="Snapshot of a golfer following through on a drive"><span></span></div>
</main>
</body>
</html>
```